Rebrand stationary with recently completed logo design

Need new business cards, thank you cards, letterhead, envelopes and presentation folders. The designs will be sent to a separate production firm so I need the files to be print ready.

My contact info
Reno Vaskelind

Office 604-381-4756
Fax 604-318-5064

Email reno@glazeworks.ca
website www.glazeworks.ca

315-27140 62nd Avenue,
Langley, BC, V3K 2R8

Target Market(s)

Homeowners, businesses and contractors

Industry/Entity Type

Business

Font styles to use
Sans Serif

Colors
34a7d7

Requirements
Must have
• Like to have one side of the business card a solid color with the logo in all white. The side with all the text to be a white background
• I find the current blue on the front of the card with the white logo too dark.
Should not have
• Gradient colors

```html
<!DOCTYPE html>
<html lang="en">
<head>
<meta charset="utf-8">
<title>GlazeWorks Stationery Set</title>
<link rel="stylesheet" href="https://fonts.googleapis.com/css2?family=Lato:wght@400;700&family=Dancing+Script:wght@700&display=swap">
<style>
  :root {
    --backdrop: #cbcbcb;
    --paper: #ffffff;
    --slate: #424f5a;
    --brand-blue: #1a8fd9;
    --ink: #1f2326;
    --body-ink: #3a3f44;
    --pattern-grey: #eeeeee;
  }
  * { box-sizing: border-box; margin: 0; padding: 0; }
  html, body { width: 1200px; height: 800px; overflow: hidden; }
  body {
    position: relative;
    background: var(--backdrop);
    font-family: "Lato", Arial, sans-serif;
    color: var(--ink);
  }
  .piece { position: absolute; background: var(--paper); overflow: hidden; }
  .band { position: absolute; left: 0; bottom: 0; width: 100%; display: block; }
  .wordmark {
    font-family: "Lato", Arial, sans-serif;
    font-weight: 700;
    color: var(--slate);
    white-space: nowrap;
    letter-spacing: 0.2px;
  }

  /* Business card – contact side */
  .card-front { left: 54px; top: 90px; width: 250px; height: 144px; }
  .card-front .holder { position: absolute; left: 21px; top: 17px; font-size: 10px; }
  .card-front .contact-list { position: absolute; left: 21px; top: 56px; list-style: none; font-size: 7.4px; }
  .card-front .contact-list li { display: flex; align-items: center; gap: 5px; height: 11px; }
  .card-front .contact-list svg { width: 8px; height: 8px; fill: var(--brand-blue); }
  .card-front .address { position: absolute; left: 21px; top: 104px; font-size: 7.4px; line-height: 10.4px; }
  .card-front .wordmark { position: absolute; right: 19px; top: 104px; font-size: 12px; }

  /* Business card – solid side */
  .card-back { left: 54px; top: 292px; width: 250px; height: 143px; background: var(--slate); }
  .card-back .wordmark {
    position: absolute; left: 0; right: 0; top: 56px; text-align: center;
    font-size: 25px; color: var(--paper);
  }

  /* Pattern card */
  .card-pattern { left: 54px; top: 486px; width: 250px; height: 143px; }
  .card-pattern .pattern-field { position: absolute; inset: 0; background: var(--pattern-grey); }
  .card-pattern .wordmark { position: absolute; right: 21px; top: 94px; font-size: 17px; }

  /* Letterhead */
  .letterhead { left: 335px; top: 90px; width: 374px; height: 483px; }
  .letterhead .masthead-mark { position: absolute; left: 37px; top: 30px; font-size: 16px; }
  .letterhead .masthead-address {
    position: absolute; left: 221px; top: 31px; font-size: 4.6px; line-height: 6px; color: var(--ink);
  }
  .letterhead .masthead-divider { position: absolute; left: 278px; top: 22px; width: 0.6px; height: 30px; background: #b9bec2; }
  .letterhead .masthead-contact { position: absolute; left: 284px; top: 24px; list-style: none; font-size: 4.4px; }
  .letterhead .masthead-contact li { display: flex; align-items: center; gap: 3px; height: 7px; }
  .letterhead .masthead-contact svg { width: 5px; height: 5px; fill: var(--brand-blue); }
  .letterhead .letter-body {
    position: absolute; left: 35px; top: 86px; width: 304px;
    font-size: 5.9px; line-height: 12.8px; color: var(--body-ink);
  }
  .letter-body .subject { font-weight: 700; color: var(--ink); margin-bottom: 12px; }
  .letter-body p { margin-bottom: 12.8px; }
  .letter-body .signature {
    width: 92px; height: 30px; margin: 2px 0 4px; background: #e6e8ea; border-radius: 2px;
  }

  /* Envelope – front */
  .envelope-front { left: 737px; top: 90px; width: 409px; height: 184px; }
  .envelope-front .wordmark { position: absolute; left: 14px; top: 16px; font-size: 11px; }
  .envelope-front .divider { position: absolute; left: 95px; top: 15px; width: 0.6px; height: 18px; background: #b9bec2; }
  .envelope-front .address { position: absolute; left: 100px; top: 16px; font-size: 5.8px; line-height: 7.4px; }

  /* Envelope – flap side */
  .envelope-back { left: 737px; top: 302px; width: 409px; height: 184px; }
  .envelope-back .flap { position: absolute; left: 0; top: 0; width: 409px; height: 62px; }
  .envelope-back .wordmark {
    position: absolute; left: 0; right: 0; top: 22px; text-align: center; font-size: 13px; color: var(--paper);
  }

  /* Thank you card */
  .thank-you { left: 740px; top: 531px; width: 392px; height: 195px; }
  .thank-you .wordmark { position: absolute; right: 19px; top: 22px; font-size: 13px; }
  .thank-you .greeting {
    position: absolute; left: 22px; top: 144px;
    font-family: "Dancing Script", cursive; font-weight: 700; font-size: 20px; color: var(--brand-blue);
  }
</style>
</head>
<body>

<!-- Business card, contact side -->
<section class="piece card-front">
  <p class="holder">Reno Vaskelind</p>
  <ul class="contact-list">
    <li><svg viewBox="0 0 10 10"><path d="M2 0.5l2 2-1 1.3c.7 1.4 1.8 2.5 3.2 3.2l1.3-1 2 2-1.3 1.5C4.5 9.3.7 5.5.5 1.8z"/></svg>604-381-4756</li>
    <li><svg viewBox="0 0 10 10"><path d="M2 0h5v3H2zM0 3.5h10V10H0zM2 5v1h2V5zM5 5v1h3V5zM2 7v1h2V7zM5 7v1h3V7z"/></svg>604-318-5064</li>
    <li style="margin-top:4px"><svg viewBox="0 0 10 10"><path d="M0 2h10v6.5H0zM1 3l4 3 4-3v-.2H1z" fill-rule="evenodd"/></svg>reno@glazeworks.ca</li>
    <li><svg viewBox="0 0 10 10"><path d="M5 0a5 5 0 100 10A5 5 0 005 0zm0 1c.7.8 1.2 2 1.3 3.4H3.7C3.8 3 4.3 1.8 5 1zM1.1 5.6h1.6c.1 1.3.5 2.4 1.1 3.2A4 4 0 011.1 5.6zm0-1.2A4 4 0 013.8 1.2c-.6.8-1 1.9-1.1 3.2zm2.6 1.2h2.6C6.2 7 5.7 8.2 5 9c-.7-.8-1.2-2-1.3-3.4zm2.5 3.2c.6-.8 1-1.9 1.1-3.2h1.6a4 4 0 01-2.7 3.2zm1.1-4.4c-.1-1.3-.5-2.4-1.1-3.2a4 4 0 012.7 3.2z"/></svg>www.glazeworks.ca</li>
  </ul>
  <p class="address">315-27140 62nd Avenue,<br>Langley, BC, V3K 2R8</p>
  <span class="wordmark">GlazeWorks</span>
  <svg class="band" viewBox="0 0 250 10" height="10" preserveAspectRatio="none">
    <rect width="250" height="10" fill="var(--slate)"/>
    <polygon points="152,10 159,0 250,0 250,10" fill="var(--paper)"/>
    <polygon points="155,10 162,0 250,0 250,10" fill="var(--brand-blue)"/>
  </svg>
</section>

<!-- Business card, solid side -->
<section class="piece card-back">
  <span class="wordmark">GlazeWorks</span>
</section>

<!-- Business card, pattern side -->
<section class="piece card-pattern">
  <div class="pattern-field" role="img" aria-label="Repeating light grey brand pattern"></div>
  <span class="wordmark">GlazeWorks</span>
</section>

<!-- Letterhead -->
<section class="piece letterhead">
  <span class="wordmark masthead-mark">GlazeWorks</span>
  <p class="masthead-address">315-27140 62nd Avenue<br>Langley, BC, V3K 2R8</p>
  <span class="masthead-divider"></span>
  <ul class="masthead-contact">
    <li><svg viewBox="0 0 10 10"><path d="M2 0.5l2 2-1 1.3c.7 1.4 1.8 2.5 3.2 3.2l1.3-1 2 2-1.3 1.5C4.5 9.3.7 5.5.5 1.8z"/></svg>604-381-4756</li>
    <li><svg viewBox="0 0 10 10"><path d="M2 0h5v3H2zM0 3.5h10V10H0z"/></svg>604-318-5064</li>
    <li><svg viewBox="0 0 10 10"><path d="M0 2h10v6.5H0z"/></svg>reno@glazeworks.ca</li>
    <li><svg viewBox="0 0 10 10"><circle cx="5" cy="5" r="4.5"/></svg>www.glazeworks.ca</li>
  </ul>
  <article class="letter-body">
    <p class="subject">Lorem Ipsum is simply</p>
    <p>dummy text of the printing and typesetting industry. Lorem Ipsum has been the industry's standard dummy text ever since the 1500s, when an unknown printer took a galley of type and scrambled it to make a type specimen book. It has survived not only five centuries, but also the leap into electronic typesetting, remaining essentially unchanged.</p>
    <p>It is a long established fact that a reader will be distracted by the readable content of a page when looking at its layout. The point of using Lorem Ipsum is that it has a more-or-less normal distribution of letters, as opposed to using 'Content here, content here', making it look like readable English. Many desktop publishing packages and web page editors now use Lorem Ipsum as their default model text, and a search for 'lorem ipsum' will uncover many web sites still in their infancy. Various versions have evolved over the years, sometimes by accident, sometimes on purpose (injected humour and the like).</p>
    <p>Contrary to popular belief, Lorem Ipsum is not simply random text. It has roots in a piece of classical Latin literature from 45 BC, making it over 2000 years old. Edwin Halloran, a Latin professor at Marlow Ridge College in Vermont, looked up one of the more obscure Latin words, consectetur, from a Lorem Ipsum passage,</p>
    <div>Lorem Ipsum</div>
    <div class="signature" role="img" aria-label="Handwritten signature"></div>
    <div>Lorem Ipsum is a dummy</div>
  </article>
  <svg class="band" viewBox="0 0 374 14" height="14" preserveAspectRatio="none">
    <rect width="374" height="14" fill="var(--slate)"/>
    <polygon points="245,14 255,0 374,0 374,14" fill="var(--paper)"/>
    <polygon points="250,14 260,0 374,0 374,14" fill="var(--brand-blue)"/>
  </svg>
</section>

<!-- Envelope, address side -->
<section class="piece envelope-front">
  <span class="wordmark">GlazeWorks</span>
  <span class="divider"></span>
  <p class="address">315-27140 62nd Avenue<br>Langley, BC, V3K 2R8</p>
</section>

<!-- Envelope, flap side -->
<section class="piece envelope-back">
  <svg class="flap" viewBox="0 0 409 62">
    <path d="M0 0H409V2C404 4 402 20 399 40C397 52 392 58 380 59H29C17 58 12 52 10 40C7 20 5 4 0 2Z" fill="var(--slate)"/>
  </svg>
  <span class="wordmark">GlazeWorks</span>
</section>

<!-- Thank you card -->
<section class="piece thank-you">
  <span class="wordmark">GlazeWorks</span>
  <p class="greeting">Thank You</p>
  <svg class="band" viewBox="0 0 392 13" height="13" preserveAspectRatio="none">
    <rect width="392" height="13" fill="var(--slate)"/>
    <polygon points="261,13 270,0 392,0 392,13" fill="var(--paper)"/>
    <polygon points="265,13 274,0 392,0 392,13" fill="var(--brand-blue)"/>
  </svg>
</section>

</body>
</html>
```